Christmas Card 2021

We need a design for a Christmas Card in the format DIN A5 (148 x 210 mm). KELTO is an Austrian company with branches all over Europe. KELTO handles international claims for insurance companies. The Christmas Card will be sent to all our clients all over Europe and beyond.
The design must include our logo (see uploaded file). The color blue that we use is: CMYK: 100/16/0/27 or RGB: 0/114/168.
The card must have this text:
Fröhliche Weihnachten und ein gutes neues Jahr!
Merry Christmas and Happy New Year!
Joyeux Noël et bonne année !
Optional you can use our key visual (see uploaded file).
Optional you can use our motto text: worldwide claims service
We are looking forward to your design!
Kind regards
Lukas

```html
<!DOCTYPE html>
<html lang="en">
<head>
<meta charset="utf-8">
<title>KELTO Christmas Card 2021</title>
<link rel="stylesheet" href="https://fonts.googleapis.com/css2?family=Cinzel:wght@400;600&display=swap">
<style>
  :root {
    --backdrop: #e9ebf0;
    --card-top: #f7f8fb;
    --card-bottom: #dcdfe9;
    --greeting-blue: #2f78cf;
    --frame-white: #ffffff;
    --logo-white: #ffffff;
    --visual-silver: #c9ccd6;
    --visual-blue: #2b5fc4;
  }
  * { margin: 0; padding: 0; box-sizing: border-box; }
  html, body {
    width: 1195px;
    height: 1200px;
    overflow: hidden;
    background: var(--backdrop);
  }
  .card {
    position: absolute;
    left: 209px;
    top: 50px;
    width: 776px;
    height: 1100px;
    background: linear-gradient(180deg, var(--card-top) 30%, var(--card-bottom) 100%);
    box-shadow: 0 6px 20px rgba(40, 60, 100, 0.18);
    overflow: hidden;
  }
  .key-visual {
    position: absolute;
    left: 0;
    top: 0;
    width: 776px;
    height: 330px;
  }
  .frame {
    position: absolute;
    inset: 16px;
    border: 2px solid var(--frame-white);
    pointer-events: none;
  }
  .greetings {
    position: absolute;
    left: 0;
    right: 0;
    top: 478px;
    text-align: center;
    font-family: "Cinzel", serif;
    color: var(--greeting-blue);
    font-size: 40px;
    line-height: 46px;
    letter-spacing: 0.5px;
  }
  .greeting { margin-bottom: 46px; }
  .greeting span { display: block; }
  .logo-name {
    position: absolute;
    left: 0;
    right: 0;
    top: 990px;
    text-align: center;
    font-family: "Cinzel", serif;
    font-weight: 600;
    font-size: 42px;
    letter-spacing: 2px;
    color: var(--logo-white);
  }
</style>
</head>
<body>
  <main class="card">
    <svg class="key-visual" viewBox="0 0 776 330" role="img" aria-label="Key visual: blue glitter Christmas baubles with blue ribbon on silver tinsel, reflected on a pale surface">
      <defs>
        <linearGradient id="tinselFade" x1="0" y1="0" x2="0" y2="1">
          <stop offset="0" stop-color="var(--visual-silver)"/>
          <stop offset="0.55" stop-color="#d8dbe3"/>
          <stop offset="1" stop-color="var(--card-top)" stop-opacity="0"/>
        </linearGradient>
        <radialGradient id="baubleGlow" cx="0.22" cy="0.5" r="0.35">
          <stop offset="0" stop-color="var(--visual-blue)" stop-opacity="0.55"/>
          <stop offset="1" stop-color="var(--visual-blue)" stop-opacity="0"/>
        </radialGradient>
      </defs>
      <rect width="776" height="330" fill="url(#tinselFade)"/>
      <rect width="776" height="330" fill="url(#baubleGlow)"/>
    </svg>

    <div class="frame"></div>

    <section class="greetings">
      <p class="greeting" lang="de"><span>Fröhliche Weihnachten</span><span>und ein gutes neues Jahr!</span></p>
      <p class="greeting" lang="en"><span>Merry Christmas</span><span>and Happy New Year!</span></p>
      <p class="greeting" lang="fr"><span>Joyeux Noël</span><span>et bonne année !</span></p>
    </section>

    <div class="logo-name">KELTO</div>
  </main>
</body>
</html>
```